GLOW ON THE AVENUE WEBSITE

I have a website www.glowontheavenue.org , need information from that jazzed up. wanted page to be fun & funky .

Target Market(s)

18 to 35yrs guys & girls

Requirements
Must have
• use all photos on website, need to attached my brochure for printing

```html
<!DOCTYPE html>
<html lang="en">
<head>
<meta charset="utf-8">
<title>Glow on the Avenue</title>
<link href="https://fonts.googleapis.com/css2?family=Rokkitt:wght@400;500&family=Roboto:wght@300;400&display=swap" rel="stylesheet">
<style>
:root{
  --red:#d0070d;
  --dark:#3d3e41;
  --footer:#3a3b3d;
  --ink:#3a3a3a;
  --white:#ffffff;
  --line:#d6d6d6;
  --skin-light:#f3ebe6;
  --skin-mid:#e2cdc2;
  --hair:#d9cbb8;
}
*{margin:0;padding:0;box-sizing:border-box}
html,body{width:1200px;height:861px;overflow:hidden;background:var(--white)}
body{position:relative;font-family:"Roboto",sans-serif;color:var(--ink)}
.hero-photo{position:absolute;left:520px;top:0;width:680px;height:796px;
  background:
   linear-gradient(90deg,var(--white) 0%,rgba(255,255,255,0) 28%),
   radial-gradient(ellipse at 55% 40%,var(--skin-light) 0%,var(--skin-mid) 55%,var(--hair) 100%);}
.top-band{position:absolute;left:0;top:54px;width:1200px;height:31px;background:var(--red)}
.logo-card{position:absolute;left:160px;top:0;width:243px;height:132px;
  background:linear-gradient(#f7f7f7,#e9e9e9);box-shadow:0 6px 6px -3px rgba(0,0,0,.35);
  display:flex;align-items:center;justify-content:center;text-align:center}
.logo-name{font-family:"Rokkitt",serif;font-weight:500;font-size:26px;line-height:1.05;color:var(--red)}
.call-box{position:absolute;left:727px;top:0;width:311px;height:38px;background:#f2f2f2;
  border:1px solid var(--line);border-top:0;font-family:"Rokkitt",serif;font-size:22px;
  line-height:38px;text-align:center;color:var(--ink)}
.main-nav{position:absolute;left:546px;top:54px;height:31px;display:flex;gap:20px;align-items:center}
.main-nav a{font-family:"Rokkitt",serif;font-weight:500;font-size:14px;color:var(--white);text-decoration:none;letter-spacing:.2px}
.headline{position:absolute;left:189px;top:256px;font-family:"Rokkitt",serif;line-height:1}
.headline .l1{font-size:33px;color:var(--ink);font-weight:500}
.headline .l2{font-size:40px;color:var(--red);font-weight:500;margin-top:2px}
.headline .l3{font-size:48px;color:var(--ink);font-weight:400;letter-spacing:1px}
.panel{position:absolute;top:499px;width:246px;height:130px;background:rgba(255,255,255,.85);padding:6px}
.panel-inner{position:relative;width:100%;height:118px;padding:10px 13px;color:var(--white)}
.panel.about{left:162px}.panel.services{left:414px}.panel.book{left:666px}
.about .panel-inner,.book .panel-inner{background:var(--dark)}
.services .panel-inner{background:var(--red)}
.panel h2{font-family:"Rokkitt",serif;font-weight:400;font-size:20px;line-height:1;margin-bottom:6px;letter-spacing:-.6px;white-space:nowrap}
.about h2{font-size:18px;letter-spacing:-.7px}
.panel p{font-size:11px;line-height:14px;letter-spacing:.2px}
.service-list{display:grid;grid-template-columns:114px 1fr;list-style:none;font-size:11px;line-height:19px;letter-spacing:.3px}
.book .panel-inner{padding-left:17px}
.book h2{font-size:30px;line-height:30px;margin-top:16px;font-weight:500;letter-spacing:-1.2px}
.more{position:absolute;right:8px;bottom:-8px;width:30px;height:28px;display:flex;align-items:center;justify-content:center;box-shadow:1px 1px 2px rgba(0,0,0,.3)}
.about .more,.book .more{background:var(--red)}
.services .more{background:var(--dark)}
.newsletter{position:absolute;left:167px;top:652px;display:flex;align-items:center;gap:12px;font-family:"Rokkitt",serif;font-size:19px;color:var(--ink)}
.signup{position:absolute;left:162px;top:685px;display:flex;gap:11px}
.signup input{width:348px;height:32px;border:1px solid var(--line);padding:0 11px;font:300 11px "Roboto",sans-serif;color:#555}
.signup button{width:94px;height:32px;background:var(--red);color:var(--white);border:0;font:400 15px "Roboto",sans-serif}
.tabs{position:absolute;left:401px;top:759px;display:flex;gap:2px}
.tab{width:210px;height:37px;background:linear-gradient(#ffffff,#ececec);border:1px solid var(--line);border-bottom:0;
  display:flex;align-items:center;justify-content:flex-end;gap:26px;padding-right:24px;font-family:"Rokkitt",serif;font-size:19px;color:#222}
.tab .up{width:25px;height:22px;background:var(--dark);display:flex;align-items:center;justify-content:center;box-shadow:1px 1px 2px rgba(0,0,0,.4)}
.site-footer{position:absolute;left:0;top:796px;width:1200px;height:65px;background:var(--footer);color:var(--white)}
.copyright{position:absolute;left:162px;top:25px;font-size:12px;font-weight:300}
.follow{position:absolute;right:163px;top:25px;display:flex;align-items:center;gap:9px;font-size:11px}
.follow span.dot{width:14px;height:14px;border-radius:50%;background:var(--white)}
</style>
</head>
<body>
<div class="hero-photo" role="img" aria-label="Close portrait of a woman with long fair hair, soft skin tones"></div>
<div class="top-band"></div>

<header>
  <div class="logo-card"><div class="logo-name">GLOW ON<br>THE AVENUE</div></div>
  <div class="call-box">CALL US TODAY! 123-555-0147</div>
  <nav class="main-nav">
    <a href="#">HOME</a><a href="#">WAXING</a><a href="#">SERVICES</a><a href="#">TESTIMONIALS</a><a href="#">AWARDS</a><a href="#">CONTACT US</a>
  </nav>
</header>

<h1 class="headline">
  <div class="l1">THE NATURAL</div>
  <div class="l2">PERSONAL CARE</div>
  <div class="l3">OF YOUR BODY</div>
</h1>

<section class="panel about">
  <div class="panel-inner">
    <h2>About Glow on the Avenue</h2>
    <p>Lorem Ipsum is simply dummy text of the printing and typesetting industry. Lorem Ipsum has been the industry's standard dummy text ever...</p>
    <span class="more"><svg width="12" height="8"><path d="M0 0h12L6 8z" fill="#fff"/></svg></span>
  </div>
</section>
<section class="panel services">
  <div class="panel-inner">
    <h2>Serivces</h2>
    <ul class="service-list">
      <li>Waxing</li><li>Massage &amp; Facial</li>
      <li>City Brow Bar</li><li>Makeup</li>
      <li>Tanning</li><li>Eyes Lash</li>
      <li>Handds &amp; Feet</li>
    </ul>
    <span class="more"><svg width="12" height="8"><path d="M0 0h12L6 8z" fill="#fff"/></svg></span>
  </div>
</section>
<section class="panel book">
  <div class="panel-inner">
    <h2>BOOK A<br>APPOINTMENT</h2>
    <span class="more"><svg width="12" height="8"><path d="M0 0h12L6 8z" fill="#fff"/></svg></span>
  </div>
</section>

<div class="newsletter">
  <svg width="22" height="18" viewBox="0 0 22 18"><path d="M1 7 11 1l10 6v10H1z" fill="#ddd"/><path d="M1 7l10 6 10-6" fill="none" stroke="#bbb"/></svg>
  STAY ON TREND WITH OUR FREE NEWSLETTER
</div>
<form class="signup">
  <input type="text" placeholder="Enter Your Email ID Here....">
  <button type="button">SIGN UP</button>
</form>

<div class="tabs">
  <div class="tab">VIDEO LINK<span class="up"><svg width="10" height="6"><path d="M0 6h10L5 0z" fill="#fff"/></svg></span></div>
  <div class="tab">LOCATIONS<span class="up"><svg width="10" height="6"><path d="M0 6h10L5 0z" fill="#fff"/></svg></span></div>
  <div class="tab">CONTACT US<span class="up"><svg width="10" height="6"><path d="M0 6h10L5 0z" fill="#fff"/></svg></span></div>
</div>

<footer class="site-footer">
  <div class="copyright">©&nbsp; All Rights Are Reserved.Glow on the Avenue.2013</div>
  <div class="follow">Follow Us: <span class="dot"></span><span class="dot"></span></div>
</footer>
</body>
</html>
```